Geschäftspapiere für Bauunternehmen
Zielgruppe
Wir sind ein Bauunternehmen.
Aufgabenstellung
Bitte das Briefpapier alles nötige für eine Angebotserstellung sowie Rechnungsstellung hinzufügen. Heißt: Logo, Firma, Firmensitz, Telefonnummer, Steuernummer und Bankdaten. Bankdaten: DE41 5108 0060 2294 7731 08 BIC: RQTNDEM1XXX

```html
<!DOCTYPE html>
<html lang="de">
<head>
<meta charset="utf-8">
<title>Harvento Bau – Briefpapier</title>
<link href="https://fonts.googleapis.com/css2?family=Montserrat:wght@400;500;600&display=swap" rel="stylesheet">
<style>
  :root {
    --red: #d90000;
    --red-bright: #ff0a0a;
    --red-dark: #1a0206;
    --ink: #111111;
    --muted: #777777;
    --faint: #f8efef;
    --paper: #ffffff;
  }
  * { margin: 0; padding: 0; box-sizing: border-box; }
  html, body { width: 949px; height: 1200px; overflow: hidden; background: var(--paper); }
  .letterhead {
    position: relative; width: 949px; height: 1200px;
    font-family: "Montserrat", sans-serif; color: var(--ink); background: var(--paper);
  }
  .brand {
    position: absolute; left: 108px; top: 200px; width: 400px;
    display: flex; align-items: center; justify-content: center; gap: 14px;
  }
  .brand-square { width: 34px; height: 34px; background: var(--red); flex: none; }
  .brand-name { font-size: 40px; font-weight: 400; letter-spacing: 1px; color: var(--ink); white-space: nowrap; }
  .divider { position: absolute; left: 590px; top: 80px; width: 2px; height: 214px; background: var(--ink); }
  .contact { position: absolute; left: 606px; top: 88px; width: 330px; }
  .contact-title { font-size: 27px; font-weight: 600; margin-left: 8px; margin-bottom: 14px; }
  .contact-item { display: flex; align-items: center; gap: 10px; font-size: 14.5px; font-weight: 500; line-height: 1.15; margin-bottom: 12px; }
  .contact-item svg { width: 20px; height: 20px; flex: none; fill: var(--red); }
  .watermark {
    position: absolute; left: 96px; top: 530px; width: 732px; text-align: center;
    font-size: 92px; font-weight: 600; letter-spacing: 4px; color: var(--faint); line-height: 1.1;
  }
  .closing { position: absolute; left: 40px; top: 890px; font-size: 14.5px; color: var(--muted); }
  .closing p { margin-bottom: 22px; }
  .signature {
    position: absolute; left: 40px; top: 980px; width: 345px; height: 70px;
    background: linear-gradient(90deg, #e8e8e8, #f6f6f6);
  }
  .role { position: absolute; left: 40px; top: 1081px; font-size: 14.5px; color: var(--muted); }
  .footer-brand {
    position: absolute; right: 30px; top: 1118px;
    display: flex; align-items: center; gap: 8px;
  }
  .footer-brand .brand-square { width: 18px; height: 18px; }
  .footer-brand .brand-name { font-size: 20px; font-weight: 400; }
  .footer-band {
    position: absolute; left: 0; top: 1160px; width: 949px; height: 24px;
    background: linear-gradient(90deg, var(--red-dark), #8a0004 40%, var(--red) 70%, var(--red-bright));
  }
</style>
</head>
<body>
<main class="letterhead">
  <div class="brand">
    <span class="brand-square"></span>
    <span class="brand-name">HARVENTO BAU</span>
  </div>

  <div class="divider"></div>

  <section class="contact">
    <h1 class="contact-title">Harvento Bau</h1>
    <div class="contact-item">
      <svg viewBox="0 0 24 24"><path d="M12 3 2 12h3v9h5v-6h4v6h5v-9h3z"/></svg>
      <span>Lindenhofer Weg 42,<br>12045 Berlin, Germany</span>
    </div>
    <div class="contact-item">
      <svg viewBox="0 0 24 24"><path d="M6.6 10.8a15 15 0 0 0 6.6 6.6l2.2-2.2a1 1 0 0 1 1-.25 11.4 11.4 0 0 0 3.6.57 1 1 0 0 1 1 1V20a1 1 0 0 1-1 1A17 17 0 0 1 3 4a1 1 0 0 1 1-1h3.5a1 1 0 0 1 1 1c0 1.25.2 2.45.57 3.57a1 1 0 0 1-.25 1z"/></svg>
      <span>030 555 21 864</span>
    </div>
    <div class="contact-item">
      <svg viewBox="0 0 24 24"><path d="M2 5h20v14H2z M3.5 6.5 12 13l8.5-6.5" stroke="#fff" stroke-width="1.2"/></svg>
      <span>info@harvento-bau.de</span>
    </div>
    <div class="contact-item">
      <svg viewBox="0 0 24 24"><circle cx="12" cy="12" r="10"/><path d="M8 6c2 1 3 3 1 5s1 3 2 5M15 4c-1 2 1 3 3 4" stroke="#fff" stroke-width="1.5" fill="none"/></svg>
      <span>www.harvento-bau.de</span>
    </div>
    <div class="contact-item">
      <svg viewBox="0 0 24 24"><path d="M12 2 2 7v2h20V7zM4 10h2v8H4zm4 0h2v8H8zm4 0h2v8h-2zm4 0h2v8h-2zM2 19h20v3H2z"/></svg>
      <span>DE41 5108 0060 2294 7731 08<br>BIC: RQTNDEM1XXX</span>
    </div>
  </section>

  <div class="watermark" aria-hidden="true">HARVENTO<br>BAU</div>

  <section class="closing">
    <p>Wir sind gern für dich da. Wir schätzen unsere Kunden sehr</p>
    <p>mit freundlichen gruben</p>
  </section>

  <div class="signature" role="img" aria-label="Handschriftliche Unterschrift Harvento Bau"></div>

  <p class="role">Bauunternehmen</p>

  <div class="footer-brand">
    <span class="brand-square"></span>
    <span class="brand-name">HARVENTO BAU</span>
  </div>

  <div class="footer-band"></div>
</main>
</body>
</html>
```